Tarjetas de visita para empresa de aluminio

Empresa con mas de 40 años vendiendo perfiles de aluminio.
Somos fábrica y almacén, queremos renovar la tarjeta de presentación de nuestros comerciales dando una imgen innovadora y tecnógica mezclado con la calidez del respeto al medio ambiente.
Añado el logo de la empresa y actual cara trasera de la tarjeta de visita, el logo es el simbolo WM y la marca TRAVENIC EXTRUSION, la frase 2extrusion y lacado de aluminio" debe cambiarse por "Diseño, extrusión, lacado, anodizado y mecanizado de precisión de aluminio" o en su defecto incluir todos esos servicios que hacemos o una frase mas pegadiza.

We are an aluminium factory, we produce and stock profiles of aluminium.
we want to renew visit card of our sellers, we are looking for something that show innovation, tecnology and environment respect.
Upload our actual logo and back of visit card, logo WM and brand TRAVENIC EXTRUSION must be keept.
Text "Extrusion y lacado de aluminio" must be changed for "Diseño, extrusion, lacado, anodizado y mecanizado de precisión de aluminio" or something like that

```html
<!DOCTYPE html>
<html lang="es">
<head>
<meta charset="utf-8">
<title>Travenic Extrusion – Tarjeta de visita</title>
<link href="https://fonts.googleapis.com/css2?family=Open+Sans:ital,wght@0,400;0,700;1,400;1,700&display=swap" rel="stylesheet">
<style>
  :root {
    --page-bg: #1d1e21;
    --card-blue: #234f78;
    --brand-blue: #3f7fc0;
    --silver: #c3c9d0;
    --silver-dim: #a9b1ba;
  }
  * { box-sizing: border-box; margin: 0; padding: 0; }
  html, body {
    width: 1200px; height: 900px; overflow: hidden;
    background: var(--page-bg);
    font-family: "Open Sans", Arial, sans-serif;
  }
  .sheet {
    width: 1200px; height: 900px;
    display: flex; align-items: center; justify-content: center; gap: 60px;
  }
  .card {
    position: relative;
    width: 520px; height: 330px;
    background: var(--card-blue);
    border-radius: 22px;
    box-shadow: 0 14px 30px rgba(0,0,0,.55);
    overflow: hidden;
  }

  /* Front */
  .card-front { display: flex; align-items: center; justify-content: center; }
  .brand { display: flex; align-items: center; gap: 18px; }
  .brand-circle {
    width: 74px; height: 74px; border-radius: 50%;
    border: 5px solid var(--brand-blue);
  }
  .brand-name {
    color: var(--brand-blue);
    font-weight: 700; font-size: 30px; letter-spacing: 2px;
  }

  /* Back */
  .card-back { color: var(--silver); font-style: italic; }
  .identity {
    position: absolute; top: 56px; right: 250px;
    text-align: right;
  }
  .person-name { font-weight: 700; font-size: 18px; letter-spacing: .5px; }
  .person-role { font-size: 13px; color: var(--silver-dim); margin-bottom: 10px; }
  .address { font-size: 12.5px; line-height: 1.45; }
  .divider {
    position: absolute; top: 56px; left: 285px;
    width: 1px; height: 150px; background: var(--silver-dim); opacity: .7;
  }
  .contacts {
    position: absolute; top: 66px; left: 305px;
    list-style: none; font-size: 13px; line-height: 1.75;
  }
  .contacts li { display: flex; align-items: center; gap: 8px; }
  .contacts svg { width: 12px; height: 12px; flex: none; }
  .tagline {
    position: absolute; left: 34px; bottom: 42px;
    font-size: 12.5px; color: var(--silver-dim);
  }
</style>
</head>
<body>
<main class="sheet">
  <section class="card card-front" aria-label="Cara frontal">
    <div class="brand">
      <span class="brand-circle"></span>
      <span class="brand-name">TRAVENIC EXTRUSION</span>
    </div>
  </section>

  <section class="card card-back" aria-label="Cara trasera">
    <div class="identity">
      <p class="person-name">MARIO LUCENA ORTIZ</p>
      <p class="person-role">Comercial</p>
      <p class="address">Pol. Ind. Los Olmos-C/3 Nº 22<br>41700 DOS HERMANAS (Sevilla)<br>Apartado de Correos 245</p>
    </div>
    <span class="divider"></span>
    <ul class="contacts">
      <li><svg viewBox="0 0 12 12"><rect x="3" y="0.5" width="6" height="11" rx="1.2" fill="none" stroke="currentColor" stroke-width="1.2"/></svg>600 12 34 56</li>
      <li><svg viewBox="0 0 12 12"><path d="M2 1.5h2.5l1 2.5-1.4 1a6 6 0 0 0 3 3l1-1.4 2.5 1V10.5A1 1 0 0 1 9.5 11.5 9 9 0 0 1 1 3a1 1 0 0 1 1-1.5z" fill="currentColor"/></svg>955 00 11 22</li>
      <li><svg viewBox="0 0 12 12"><rect x="1" y="4" width="10" height="6" rx="1" fill="currentColor"/><rect x="3" y="1" width="6" height="3" fill="currentColor"/></svg>955 00 11 23</li>
      <li><svg viewBox="0 0 12 12"><rect x="0.8" y="2.5" width="10.4" height="7" rx="1" fill="none" stroke="currentColor" stroke-width="1.2"/><path d="M1 3l5 4 5-4" fill="none" stroke="currentColor" stroke-width="1.2"/></svg>mariolucena@travenic.com</li>
      <li><svg viewBox="0 0 12 12"><circle cx="6" cy="6" r="5" fill="none" stroke="currentColor" stroke-width="1.2"/><path d="M1 6h10M6 1c-2.5 3-2.5 7 0 10M6 1c2.5 3 2.5 7 0 10" fill="none" stroke="currentColor" stroke-width=".9"/></svg>www.travenic.com</li>
    </ul>
    <p class="tagline">Diseño, extrusion, lacado, anodizado y mecanizado de precisión de aluminio</p>
  </section>
</main>
</body>
</html>
```